依頼詳細
いまあるサンプルを春らしく変えて頂いても結構ですし、違うイメージで一から作成して頂いても結構です。このサンプルデザインに特にこだわりがあるわけではありませんので、良いデザインがあればどんどんご提案下さい。

対象が女性の50代~70代になるのでデザインのおしゃれさも大事ですが、シンプルでわかりやすいデザインを希望します。

A3サイズとB4サイズで作成をして下さい。
内容はまったく同じで用紙に合わせてレイアウトを調整して下さい。

真ん中部分の広告商品の商品名や価格はダミーで入れて頂ければ後から私が加筆します。

今後は季節ごとに配色を変えたり、季節感のある物を軽く挿入する程度で、作って頂いたデザインを通年使用していく予定です。

2ヶ月ごとに新聞広告の作成がありますので、今後ともよろしくお願いします。

選択させて頂いた広告の著作権(財産権)等は当方に譲渡をお願いします。フォントや画像素材などを利用する場合は上記利用用途に使用できることを確認し、第三者の知的財産権等に注意して下さい。
記載項目
会期 4月5日(火)~10日(日)

営業時間 10:00~18:00(最終日のみ15:00迄)

会場 アサギリモール一階・北側 SPACEはなゆき 京都市北区雲井南梅枝町38-6

主催 株式会社明葉 京都市北区雲井西竹丘町17-42 tel075-555-0183

2015年4月のサンプルにあるネットショップとブログの案内は省いて下さい。
サイズ
A3
ページ数
片面
希望イメージ
シンプル 複雑
単色 カラフル
暗い 明るい
日常 高級
遊び心 厳粛
未来的 伝統的
女性的 男性的
希望する色
納品ファイル
• 高解像度JPG (.jpg)
• イラストレーター形式 (.ai)
• フォトショップ形式 (.psd)
補足説明
サンプルを添付をさせて頂きます
たくさんのすばらしいデザインを作成して頂き、皆様本当にありがとうございます。

良いデザインばかりなので選定作業が困難を極めています(笑)

採用させて頂いた方はもちろん、それ以外の方も今後ともよろしくお願い申し上げます。

ありがとうございました。
■ 選んだ理由

女性のデザイナーさんらしくやさしさが伝わってきました。

■ 提案者全員のお礼・コメント

皆様本当にありがとうございました。明葉の広告をこんなたくさんの方にデザインしていただきうれしく思います。今後もよろしくお願いします。

```html
<!DOCTYPE html>
<html lang="ja">
<head>
<meta charset="utf-8">
<title>明葉の婦人服 春祭り</title>
<link rel="stylesheet" href="https://fonts.googleapis.com/css2?family=M+PLUS+Rounded+1c:wght@500;800&family=Shippori+Mincho+B1:wght@800&display=swap">
<style>
:root{
  --pink:#e5417f;
  --pink-deep:#d22a6c;
  --pink-soft:#f7cfdd;
  --pink-pale:#fbe6ee;
  --ink:#3a2a30;
  --white:#ffffff;
}
*{margin:0;padding:0;box-sizing:border-box}
html,body{width:849px;height:1200px;overflow:hidden}
body{font-family:"M PLUS Rounded 1c",sans-serif;color:var(--ink);background:var(--white)}
.flyer{position:relative;width:849px;height:1200px;overflow:hidden;
  background:linear-gradient(180deg,var(--pink-pale) 0%,var(--pink-soft) 55%,#f3bcd0 100%)}
.blossom-pattern{position:absolute;inset:0 0 230px 0;
  background:radial-gradient(circle at 50% 20%,rgba(255,255,255,.55),rgba(255,255,255,0) 60%)}
.brand{position:absolute;left:36px;top:28px;display:flex;align-items:center;gap:8px;
  color:var(--pink);font-weight:800;font-size:28px;letter-spacing:2px}
.brand .dot{width:14px;height:14px;border-radius:50%;background:var(--pink)}
.mannequin{position:absolute;left:290px;top:450px;width:170px;height:500px;border-radius:85px 85px 40px 40px;
  background:linear-gradient(180deg,#ffffff 0%,#f9dde8 70%,#e9a9c1 100%);opacity:.9}
.subtitle{position:absolute;left:288px;top:86px;writing-mode:vertical-rl;
  font-family:"Shippori Mincho B1",serif;font-weight:800;font-size:44px;color:var(--pink-deep);letter-spacing:4px}
.title{position:absolute;left:352px;top:44px;writing-mode:vertical-rl;
  font-family:"Shippori Mincho B1",serif;font-weight:800;font-size:165px;line-height:1;color:var(--pink);
  letter-spacing:-4px;text-shadow:0 0 14px rgba(255,255,255,.9)}
.date{position:absolute;border-radius:50%;background:var(--pink);color:var(--white);
  display:flex;align-items:center;justify-content:center;font-weight:800}
.date-start{left:610px;top:40px;width:180px;height:180px}
.date-end{left:660px;top:190px;width:160px;height:160px;border:4px solid var(--white)}
.date .m{font-size:36px}
.date .d{font-size:68px;line-height:1}
.date .dd{font-size:62px;line-height:1}
.date .w{display:inline-block;margin-left:4px;background:var(--white);color:var(--pink);border-radius:50%;
  width:32px;height:32px;font-size:20px;line-height:32px;text-align:center}
.hours{position:absolute;left:666px;top:356px;width:150px;text-align:center;color:var(--pink-deep);font-size:17px;font-weight:800;line-height:1.3}
.hours small{display:block;font-size:14px;font-weight:500}
.item{position:absolute;color:var(--ink);white-space:nowrap}
.item .name{font-weight:800;font-size:30px;line-height:1.1}
.item .note{font-size:13px;font-weight:500}
.item .price{font-weight:800;color:var(--pink-deep);font-size:54px;line-height:1.05;letter-spacing:-1px;
  text-shadow:2px 2px 0 var(--white),-2px -2px 0 var(--white),2px -2px 0 var(--white),-2px 2px 0 var(--white)}
.item .price small{font-size:24px;margin-left:2px}
.item .price .tax{font-size:11px;vertical-align:top;color:var(--ink);text-shadow:none;font-weight:500}
.scarf-a{left:36px;top:100px}
.scarf-b{left:36px;top:258px}
.scarf-c{left:540px;top:470px}
.cut .name{font-size:24px}
.cut .note{font-size:12px}
.cut .price{font-size:44px}
.cut .price small{font-size:20px}
.cut-1{left:470px;top:655px}
.cut-2{left:660px;top:640px}
.cut-3{left:470px;top:770px}
.cut-4{left:660px;top:755px}
.special{position:absolute;left:40px;top:425px;width:200px;padding:16px 8px;border-radius:20px;
  background:rgba(255,255,255,.88);border:3px solid var(--pink);text-align:center;
  color:var(--pink-deep);font-weight:800;font-size:28px;line-height:1.3}
.special-note{position:absolute;left:44px;top:592px;width:200px;font-size:13px;line-height:1.6;color:var(--pink-deep);font-weight:500}
.daily{position:absolute;left:460px;top:872px;color:var(--pink-deep);font-weight:800;text-align:center;width:380px;white-space:nowrap}
.daily .line1{font-size:24px;background:var(--white);border-radius:6px;padding:0 10px;display:inline-block}
.daily .line2{font-size:26px;margin-top:4px}
.footer{position:absolute;left:0;bottom:0;width:849px;height:230px;background:var(--white);display:flex;align-items:center;padding:0 24px;gap:20px}
.host{width:230px;font-size:14px;line-height:1.5}
.host .org{font-weight:800;font-size:22px}
.host .brand-small{color:var(--pink);font-weight:800;font-size:20px;letter-spacing:1px}
.host .tel{display:flex;align-items:center;gap:6px;font-weight:800;font-size:24px;color:var(--pink-deep)}
.venue{display:flex;align-items:center;gap:12px;flex:1}
.venue .badge{flex:none;width:64px;height:64px;border-radius:50%;background:var(--pink);color:var(--white);
  display:flex;align-items:center;justify-content:center;font-weight:800;font-size:20px}
.venue .place{font-size:14px;line-height:1.5}
.venue .hall{font-weight:800;font-size:28px;color:var(--pink-deep)}
.map{flex:none;width:220px;height:170px;background:linear-gradient(135deg,#f1f1f1,#dcdcdc);border:1px solid #ccc}
</style>
</head>
<body>
<main class="flyer">
  <div class="blossom-pattern" role="img" aria-label="桜の花びら模様の背景"></div>

  <div class="brand"><span class="dot"></span>ROSALIE</div>

  <div class="mannequin" role="img" aria-label="春物ワンピースを着たトルソーのイラスト"></div>

  <h2 class="subtitle">明葉の婦人服</h2>
  <h1 class="title">春祭り</h1>

  <div class="date date-start"><span class="m">4月</span><span class="d">5</span><span class="m">日</span><span class="w">火</span></div>
  <div class="date date-end"><span class="dd">10</span><span class="m">日</span><span class="w">日</span></div>
  <p class="hours">10:00～18:00<small>最終日のみ15:00迄</small></p>

  <div class="item scarf-a">
    <p class="name">スカーフ・<br>ストール各種</p>
    <p class="note">(シルク・ポリエステル・ウール他)</p>
    <p class="price">1,000<small>円～</small><span class="tax">(税込)</span></p>
  </div>
  <div class="item scarf-b">
    <p class="name">スカーフ・<br>ストール各種</p>
    <p class="note">(シルク・ポリエステル・ウール他)</p>
    <p class="price">1,000<small>円～</small><span class="tax">(税込)</span></p>
  </div>

  <div class="special">春夏商品<br>特別価格で<br>ご提供!!</div>
  <p class="special-note">その他お買い得な品々、春物・夏物のお洋服を多数ご用意しております。</p>

  <div class="item scarf-c">
    <p class="name">スカーフ・<br>ストール各種</p>
    <p class="note">(シルク・ポリエステル・ウール他)</p>
    <p class="price">1,000<small>円～</small><span class="tax">(税込)</span></p>
  </div>

  <div class="item cut cut-1"><p class="name">カットソー各種</p><p class="note">(ボーダー/ハンド他)</p><p class="price">1,000<small>円～</small></p></div>
  <div class="item cut cut-2"><p class="name">カットソー各種</p><p class="note">(ボーダー/ハンド他)</p><p class="price">1,000<small>円～</small></p></div>
  <div class="item cut cut-3"><p class="name">カットソー各種</p><p class="note">(ボーダー/ハンド他)</p><p class="price">1,000<small>円～</small></p></div>
  <div class="item cut cut-4"><p class="name">カットソー各種</p><p class="note">(ボーダー/ハンド他)</p><p class="price">1,000<small>円～</small></p></div>

  <div class="daily">
    <p class="line1">日替り特別お値打ち品</p>
    <p class="line2">均一コーナーもお楽しみに!!</p>
  </div>

  <footer class="footer">
    <div class="host">
      <p>主催</p>
      <p class="org">株式会社明葉</p>
      <p class="brand-small">ROSALIE</p>
      <p class="tel">
        <svg width="20" height="20" viewBox="0 0 24 24" aria-hidden="true"><path fill="#d22a6c" d="M6.6 10.8a15.1 15.1 0 006.6 6.6l2.2-2.2c.3-.3.7-.4 1-.2 1.1.4 2.3.6 3.6.6.6 0 1 .4 1 1V20c0 .6-.4 1-1 1A17 17 0 013 4c0-.6.4-1 1-1h3.5c.6 0 1 .4 1 1 0 1.3.2 2.5.6 3.6.1.3 0 .7-.2 1z"/></svg>
        075-555-0183</p>
      <p>rosalie-mode.jp</p>
    </div>
    <div class="venue">
      <div class="badge">会場</div>
      <div class="place">
        <p>アサギリモール1階・北側</p>
        <p class="hall">SPACEはなゆき</p>
        <p>京都市北区雲井南梅枝町38-6</p>
      </div>
    </div>
    <div class="map" role="img" aria-label="会場周辺の案内地図"></div>
  </footer>
</main>
</body>
</html>
```